business card for trucking industry consulting firm

Our company, Velkor Services Inc. provides numerous services to the trucking industry as listed on our website: velkor.ca
The logo i want on the card is the black and red VELKOR
update: i would like the services we provide listed on the card (see velkor.ca)

```html
<!DOCTYPE html>
<html lang="en">
<head>
<meta charset="utf-8">
<title>Velkor Services Inc. – Business Card</title>
<link href="https://fonts.googleapis.com/css2?family=Lato:wght@400;700;900&display=swap" rel="stylesheet">
<style>
  :root {
    --canvas: #2a2a2a;
    --card: #1e1e1e;
    --card-edge: #262626;
    --white: #f2f2f2;
    --grey: #bdbdbd;
    --red: #d3202a;
  }
  * { box-sizing: border-box; margin: 0; padding: 0; }
  html, body { width: 1200px; height: 895px; overflow: hidden; }
  body {
    background: var(--canvas);
    font-family: "Lato", sans-serif;
    color: var(--white);
    position: relative;
  }
  .card {
    position: absolute;
    width: 560px;
    height: 320px;
    background: var(--card);
    border-radius: 16px;
    overflow: hidden;
    box-shadow: 0 18px 40px rgba(0,0,0,.55);
  }
  .card--back { left: 320px; top: 100px; }
  .card--front { left: 320px; top: 470px; }

  /* Back side */
  .wordmark {
    font-family: "Lato", sans-serif;
    font-weight: 900;
    letter-spacing: 3px;
    color: var(--white);
    text-transform: uppercase;
  }
  .card--back .wordmark {
    position: absolute;
    top: 62px; left: 0; right: 0;
    text-align: center;
    font-size: 34px;
    color: var(--grey);
  }
  .services {
    position: absolute;
    top: 168px; left: 40px; right: 30px;
    display: flex;
    gap: 28px;
  }
  .services ul { list-style: none; flex: 1; }
  .services li {
    position: relative;
    padding-left: 14px;
    font-size: 13.5px;
    line-height: 20px;
    color: var(--white);
  }
  .services li::before {
    content: "";
    position: absolute;
    left: 0; top: 7px;
    width: 6px; height: 6px;
    border-radius: 50%;
    background: var(--red);
  }

  /* Front side */
  .card--front .wordmark {
    position: absolute;
    top: 40px; right: 36px;
    font-size: 28px;
  }
  .identity { position: absolute; left: 34px; top: 150px; }
  .identity__name {
    font-size: 24px;
    font-weight: 700;
    color: var(--red);
    letter-spacing: 1px;
  }
  .identity__title { font-size: 15px; margin-top: 2px; }
  .rule {
    position: absolute;
    left: 230px; right: 30px; top: 166px;
    height: 1px; background: var(--white);
  }
  .contacts { position: absolute; left: 34px; top: 210px; list-style: none; }
  .contacts li {
    display: flex; align-items: center; gap: 10px;
    font-size: 14px; line-height: 20px;
  }
  .contacts svg { width: 12px; height: 12px; fill: var(--red); }
  .contacts .accent { color: var(--red); }
  .address {
    position: absolute; right: 36px; top: 184px;
    font-size: 14px; line-height: 19px; text-align: left;
  }
  .hotline {
    position: absolute; left: 0; right: 0; bottom: 0;
    height: 34px; background: var(--red);
    display: flex; align-items: center; gap: 10px;
    padding-left: 30px;
    font-size: 15px; letter-spacing: .5px; color: var(--white);
  }
  .hotline svg { width: 15px; height: 15px; fill: var(--white); }
</style>
</head>
<body>

<section class="card card--back">
  <div class="wordmark">Velkor Services Inc.</div>
  <div class="services">
    <ul>
      <li>Prorate Licensing</li>
      <li>Safety Fitness Certificates (SFC)</li>
      <li>Log Book Auditing</li>
      <li>Compliance and Audit Assistance</li>
    </ul>
    <ul>
      <li>IFTA Fuel Tax Reporting</li>
      <li>Travel to USA</li>
      <li>Written Safety &amp; Maintenance Programs</li>
      <li>Design and Printing of Log Books and Trip Inspection books</li>
    </ul>
  </div>
</section>

<section class="card card--front">
  <div class="wordmark">Velkor Services Inc.</div>
  <div class="identity">
    <div class="identity__name">MARCUS HALE</div>
    <div class="identity__title">Founder &amp; CEO</div>
  </div>
  <div class="rule"></div>
  <ul class="contacts">
    <li><svg viewBox="0 0 12 12"><rect x="3" y="0" width="6" height="12" rx="1.2"/></svg>000 000 0000</li>
    <li><svg viewBox="0 0 12 12"><path d="M0 2h12v8H0z M0 2l6 4 6-4" /></svg>admin@<span class="accent">velkor</span>.ca</li>
    <li><svg viewBox="0 0 12 12"><circle cx="6" cy="6" r="6"/></svg>www.<span class="accent">velkor</span>.ca</li>
  </ul>
  <address class="address" style="font-style:normal">
    418, 7720-52 Ave<br>
    Edmonton, Alberta, T6B 2K9<br>
    Canada
  </address>
  <div class="hotline">
    <svg viewBox="0 0 24 24"><path d="M6.6 10.8a15.1 15.1 0 0 0 6.6 6.6l2.2-2.2a1 1 0 0 1 1-.25 11.4 11.4 0 0 0 3.6.57 1 1 0 0 1 1 1V20a1 1 0 0 1-1 1A17 17 0 0 1 3 4a1 1 0 0 1 1-1h3.5a1 1 0 0 1 1 1c0 1.25.2 2.45.57 3.57a1 1 0 0 1-.25 1z"/></svg>
    TOLL FREE 1-800-VELKOR (835-567) or LOCAL 780-555-0142
  </div>
</section>

</body>
</html>
```